KTJ Business Card

Create a Simple but Elegant business card for a Luxury Off Road Vehicle and Accessories sales Company. Center of Letters we usually fill with red or a carbon fiber we don't want to limit creativity so anything goes. I think we would prefer large logo on the front and a smaller logo with infused QR reader on the back.
Some Ideas to get you heading more in the right direction are to put them on a thicker cardstock with red edges and we would need our logo letter (KTJ) filled in with red. Example is the Vescarelli card in our brief. For the side with our info on it we are looking for our logo to include an embedded QR reader also in our brief.
Information to include 2 bullet points: Luxury Off Road Vehicle Sales / Custom Off Road Bumpers
Address:418 Pellmont Road, Suite 519, The Woodlands, Texas
Phone# 555-314-9027,
Website: WWW.KTJ-TRAILGEAR.EXAMPLE
Facebook: facebook.com/KTJTrailGear
Instagram: instagram.com/ktj_trailgear
Target Market(s)
Exotic Vehicle and Outdoor enthusiasts.
Industry/Entity Type
Business
Look and feel
Each slider illustrates characteristics of the customer's brand and the style your logo design should communicate.

```html
<!DOCTYPE html>
<html lang="en">
<head>
<meta charset="utf-8">
<title>KTJ Business Card</title>
<link href="https://fonts.googleapis.com/css2?family=Arimo:wght@400;700&family=Michroma&display=swap" rel="stylesheet">
<style>
  :root {
    --backdrop: #e9e9ea;
    --card: #141213;
    --card-edge: #0a0909;
    --gold: #c9a93a;
    --gold-soft: #b8982f;
  }
  * { margin: 0; padding: 0; box-sizing: border-box; }
  html, body { width: 1200px; height: 800px; overflow: hidden; }
  body {
    background: var(--backdrop);
    font-family: "Arimo", Arial, sans-serif;
    position: relative;
  }
  .card {
    position: absolute;
    width: 540px;
    height: 310px;
    background: var(--card);
    border: 1px solid var(--card-edge);
    color: var(--gold);
  }
  .card--front { left: 40px; top: 90px; }
  .card--back { left: 620px; top: 400px; }

  .brand {
    position: absolute;
    display: flex;
    align-items: center;
    gap: 12px;
  }
  .brand__name {
    font-family: "Arimo", Arial, sans-serif;
    font-weight: 700;
    color: var(--gold);
    letter-spacing: 4px;
    line-height: 1;
  }
  .brand__dot {
    border-radius: 50%;
    border: 4px solid var(--gold);
  }
  .card--front .brand { left: 170px; top: 95px; }
  .card--front .brand__name { font-size: 72px; }
  .card--front .brand__dot { width: 62px; height: 62px; }

  .tagline {
    position: absolute;
    font-family: "Michroma", sans-serif;
    font-size: 12px;
    letter-spacing: 2px;
    color: var(--gold);
    text-transform: uppercase;
    white-space: nowrap;
  }
  .card--front .tagline { left: 172px; top: 178px; }

  .services {
    position: absolute;
    left: 60px;
    bottom: 48px;
    display: flex;
    gap: 40px;
    list-style: none;
    font-size: 15px;
    color: var(--gold);
  }
  .services li::before {
    content: "";
    display: inline-block;
    width: 5px; height: 5px;
    border-radius: 50%;
    background: var(--gold);
    margin-right: 8px;
    vertical-align: middle;
  }

  .card--back .brand { left: 38px; top: 128px; }
  .card--back .brand__name { font-size: 50px; }
  .card--back .brand__dot { width: 44px; height: 44px; border-width: 3px; }
  .card--back .tagline { left: 40px; top: 186px; font-size: 8px; letter-spacing: 1px; }

  .divider {
    position: absolute;
    left: 290px;
    top: 50px;
    width: 1px;
    height: 210px;
    background: linear-gradient(to bottom, transparent, var(--gold-soft) 30%, var(--gold-soft) 70%, transparent);
  }

  .contact {
    position: absolute;
    left: 314px;
    top: 62px;
    font-size: 13px;
    line-height: 1.35;
    color: var(--gold);
  }
  .contact__address { margin-bottom: 22px; }
  .contact__list { list-style: none; }
  .contact__list li {
    display: flex;
    align-items: center;
    gap: 8px;
    margin-bottom: 3px;
    white-space: nowrap;
  }
  .contact__icon { width: 14px; height: 14px; flex: none; }
  .contact__mark {
    width: 13px; height: 13px; flex: none;
    background: var(--gold);
    border-radius: 3px;
  }
</style>
</head>
<body>
  <section class="card card--front" aria-label="Business card front">
    <div class="brand">
      <span class="brand__name">KTJ</span>
      <span class="brand__dot"></span>
    </div>
    <p class="tagline">Custom Off-Road Products</p>
    <ul class="services">
      <li>Luxury Off Road Vehicle Sales</li>
      <li>Custom Off Road Bumpers</li>
    </ul>
  </section>

  <section class="card card--back" aria-label="Business card back">
    <div class="brand">
      <span class="brand__name">KTJ</span>
      <span class="brand__dot"></span>
    </div>
    <p class="tagline">Custom Off-Road Products</p>
    <div class="divider"></div>
    <div class="contact">
      <p class="contact__address">418 Pellmont Road, Suite 519<br>The Woodlands, Texas</p>
      <ul class="contact__list">
        <li>
          <svg class="contact__icon" viewBox="0 0 16 16" aria-hidden="true">
            <path d="M3 2h3l1 3-2 1.5a9 9 0 0 0 4.5 4.5L11 9l3 1v3a1 1 0 0 1-1 1A12 12 0 0 1 2 3a1 1 0 0 1 1-1z" fill="currentColor"/>
          </svg>
          555-314-9027
        </li>
        <li><span class="contact__mark"></span>facebook.com/KTJTrailGear</li>
        <li><span class="contact__mark"></span>instagram.com/ktj_trailgear</li>
        <li>
          <svg class="contact__icon" viewBox="0 0 16 16" aria-hidden="true" fill="none" stroke="currentColor" stroke-width="1.4">
            <circle cx="8" cy="8" r="6.5"/>
            <ellipse cx="8" cy="8" rx="3" ry="6.5"/>
            <line x1="1.5" y1="8" x2="14.5" y2="8"/>
          </svg>
          www.ktj-trailgear.example
        </li>
      </ul>
    </div>
  </section>
</body>
</html>
```